Book Marketing Site for authors needs redesign

I need a site redesign for the site www.quornvale.com I would like to have it designed/created in Wordpress so that I can change/edit the text as necessary. Ideally, we can simplify the site so that Wordpress updates do not impact the functionality of the site.

I want to continue to use the Quornvale logo, so I would like the site to work the existing logo. I am also planning to add the tag line Reader Outreach Made Plain so please incorporate the tag line with the logo and the site.

Initially, I would like to see the page design template and then once that is approved, you to program the site. Wherever, I have indicated that we would capture email addresses; I would like to set it up so that the names are captured in my Mailwick Hub account.

Below are the elements that will need to be part of the site:
_______

Elements that should be above the fold:

• Chirpnet, Friendwall, Orbix+ and Workloop buttons with the copy “Connect with Dorothy”
o
• The copy “Sign up for our free newsletter and receive our list of Top Chirpnet Tips for Authors Free!” with a box to enter email address. The button should say “Go” not "Submit".
• A space/box for a short, 10-15 word testimonials. The testimonials will need to change from page to page.

Nav Bar/sub nav bars

Services
Packages Speaking Testimonials
FAQ
-
About Us
Speaking
-
Resources
-
Our clients
Testimonials
-
Blog
-
Contact Us

Home page
• Should have the following copy:
High Impact Book Marketing for Authors

Quornvale Marketing is book marketing service that that provides authors with an effective,
affordable approach to marketing their book.

We provide marketing coaching and consulting services that accelerate book sales, target your ideal reader and develop a community of fans that will promote your book for you.

Using high impact, low cost marketing strategies, we will develop a book marketing strategy that achieves your goals and accommodates your budget

Do you
• Want to be a best selling author, but need someone to show you the way

• Wonder what is the secret to achieving high book sales?

• Worry that you aren’t doing the right things to ensure that your book is a success?

• Need someone to help keep your spirits up and maintain momentum?

• Please put the following copy in a box at the bottom of the copy.
o Are you ready for results? Call now for a free consultation 214-555-0183

Services Page
• Copy to come

Packages Page

FAQ Page
• Same as existing site

About page
• Same as existing site

Speaking Page

Speaking

If you’re looking to create an exceptional program that your attendees won’t be able to stop talking about, you have found it!

Dorothy Pellam, a leader in book marketing, has ability to make sophisticated internet concepts easy and accessible, and the unique ability to not only to inform, but also to inspire. Her presentations leave participants with tangible, actionable ideas proven to increase book sales.

Dorothy's talks combine practical step-by-step instructions, real-life examples with plenty of humor. Call 214-555-0183 to book her now!

Dorothy’s most popular talks:

• Unlocking the Power of Pagehive
• How to Simplify Social Media
• The Ideal Author Website
• Bazario: What You Need to Know to Succeed

Resources page
• Same as existing site

Clients
• Same as existing site

Testimonials
• I would like to be able to put a image of book cover next to the testimonial on this page.

Blog page
• Please add the following elements:
• A way to sign up for the blog via RSS
o Each blog article should have a way to Friendwall like, Tweet, O+, Pokk and Trundlefind the article

Contact us page
• Same as existing site

Site Map
• Please make sure to include a site map.

Chirpnet and Friendwall headers
• Please provide both with consistent branding.

Target Market(s)

Clients are both traditionally and indie published authors trying to be the next M.K. Orwin!

Industry/Entity Type

Marketing

Requirements
Must have
• Elements that should be above the fold:

o

```html
<!DOCTYPE html>
<html lang="en">
<head>
<meta charset="utf-8">
<title>quornvale.com – Reader Outreach Made Plain</title>
<link href="https://fonts.googleapis.com/css2?family=Open+Sans:wght@300;400;600;700;800&display=swap" rel="stylesheet">
<style>
:root{
  --green:#7bbb1f;
  --text:#555;
  --muted:#8a8a8a;
  --light:#aaa;
  --line:#e6e6e6;
  --hero:#353535;
  --panel:#f4f4f4;
  --footer:#f5f5f5;
  --bar:#a2a2a2;
  --white:#fff;
}
*{margin:0;padding:0;box-sizing:border-box}
html,body{width:1014px;height:1200px;overflow:hidden;background:var(--white)}
body{font-family:"Open Sans",Arial,sans-serif;color:var(--text);position:relative}

/* header */
.site-header{position:absolute;left:0;top:0;width:1014px;height:64px;background:var(--white)}
.logo{position:absolute;left:64px;top:12px;font-size:24px;line-height:28px;color:var(--green);font-weight:400}
.tagline{position:absolute;left:65px;top:41px;font-size:9.5px;letter-spacing:.4px;color:var(--light)}
.main-nav{position:absolute;left:498px;top:0;height:64px;display:flex}
.main-nav a{display:block;height:64px;line-height:64px;font-size:11px;color:#777;text-decoration:none;padding:0 13px;white-space:nowrap}
.main-nav a.active{background:#f6f6f6;border-bottom:3px solid var(--green);width:56px;padding:0;text-align:center}
.main-nav .caret{display:inline-block;margin-left:4px;width:5px;height:5px;border-right:1px solid #bbb;border-bottom:1px solid #bbb;transform:rotate(45deg) translateY(-3px)}

/* hero */
.hero{position:absolute;left:0;top:64px;width:1014px;height:338px;background:var(--hero);overflow:hidden}
.hero-title{position:absolute;left:64px;top:108px;font-size:31px;line-height:40px;font-weight:800;color:var(--white)}
.hero-sub{position:absolute;left:64px;top:147px;font-size:19px;line-height:26px;font-weight:300;color:#ddd}
.hero-text{position:absolute;left:64px;top:185px;width:290px;font-size:12.5px;line-height:19px;color:#bbb}
.hero-media{position:absolute;left:400px;top:16px;width:540px;height:322px;border-radius:14px 14px 0 0;background:linear-gradient(180deg,#f2f2f2 0%,#e2e2e2 60%,#c9b8a8 100%)}
.hero-arrow{position:absolute;top:135px;width:36px;height:53px;background:#4a4a4a}
.hero-arrow.left{left:0}
.hero-arrow.right{right:0}
.hero-arrow svg{position:absolute;left:12px;top:19px}

/* features */
.feature{position:absolute;top:447px;width:280px}
.feature-icon{position:absolute;left:0;top:0;width:46px;height:46px;border-radius:50%;background:#eee}
.feature-icon svg{position:absolute;left:15px;top:15px}
.feature h3{position:absolute;left:61px;top:0;font-size:15.5px;font-weight:400;color:#555;white-space:nowrap}
.feature p{position:absolute;left:61px;top:25px;width:220px;font-size:11.3px;line-height:19px;color:var(--muted)}

/* section headings */
.section-title{position:absolute;left:64px;font-size:14.5px;font-weight:400;color:#555;background:var(--white);padding-right:14px}
.section-rule{position:absolute;height:1px;background:var(--line)}
.work-nav{position:absolute;top:551px;width:18px;height:18px}
.work-nav.prev{left:912px;background:#e8e8e8}
.work-nav.next{left:932px;background:#b5b5b5}
.work-nav svg{position:absolute;left:6px;top:5px}

/* talk cards */
.work-card{position:absolute;top:587px;width:210px;height:215px;background:var(--panel)}
.work-image{width:210px;height:150px}
.work-card h4{position:absolute;left:0;top:164px;width:100%;text-align:center;font-size:12.5px;font-weight:400;color:#555;white-space:nowrap}
.work-card span{position:absolute;left:0;top:184px;width:100%;text-align:center;font-size:10px;color:var(--light)}

/* clients */
.clients-arrow{position:absolute;top:894px}
.client{position:absolute;top:887px;height:28px;display:flex;align-items:center;gap:6px;font-size:18px;font-weight:600;color:#777}
.client .mark{width:20px;height:20px;border-radius:50%;border:2px solid #888}

/* footer */
.site-footer{position:absolute;left:0;top:954px;width:1014px;height:198px;background:var(--footer)}
.foot-col{position:absolute;top:32px;width:210px}
.foot-col h5{font-size:15px;font-weight:400;color:#555;margin-bottom:10px}
.foot-col p{font-size:11px;line-height:18px;color:var(--muted)}
.quote{position:relative;padding-left:21px}
.quote svg{position:absolute;left:0;top:4px}
.quote cite{display:block;font-style:normal;font-weight:600;color:#777;margin-top:4px}
.contact-row{position:relative;padding-left:21px;font-size:11px;color:var(--muted);line-height:18px}
.contact-row b{font-weight:600;color:#777}
.contact-row svg{position:absolute;left:1px;top:4px}
.newsletter-form{position:absolute;left:0;top:92px;width:210px;height:28px;display:flex}
.newsletter-form .field{width:172px;height:28px;background:var(--white);border:1px solid #e2e2e2;font-size:10.5px;color:#aaa;line-height:26px;padding-left:9px}
.newsletter-form .go{width:38px;height:28px;background:var(--green);color:var(--white);font-size:11px;font-weight:600;text-align:center;line-height:28px}

.bottom-bar{position:absolute;left:0;top:1152px;width:1014px;height:48px;background:var(--bar)}
.copyright{position:absolute;left:64px;top:16px;font-size:10.5px;color:var(--white)}
.social{position:absolute;right:64px;top:16px;display:flex;gap:10px;font-size:10.5px;color:var(--white)}
.social .connect{font-weight:400;margin-right:4px}
.social span{font-weight:600}
</style>
</head>
<body>

<header class="site-header">
  <div class="logo">quornvale.com</div>
  <div class="tagline">Reader Outreach Made Plain</div>
  <nav class="main-nav">
    <a class="active">Home</a>
    <a>Services<i class="caret"></i></a>
    <a>About Us<i class="caret"></i></a>
    <a>Resources<i class="caret"></i></a>
    <a>Blog</a>
    <a>Contact Us</a>
  </nav>
</header>

<section class="hero">
  <div class="hero-arrow left"><svg width="10" height="14" viewBox="0 0 10 14"><path d="M8 1 2 7l6 6" fill="none" stroke="#888" stroke-width="2.5"/></svg></div>
  <h1 class="hero-title">HIGH IMPACT</h1>
  <h2 class="hero-sub">BOOK MARKETING FOR AUTHORS</h2>
  <p class="hero-text">Quornvale Marketing gives authors an effective, affordable approach to marketing their book.</p>
  <div class="hero-media" role="img" aria-label="Two hands holding a white tablet playing an embedded video"></div>
  <div class="hero-arrow right"><svg width="10" height="14" viewBox="0 0 10 14"><path d="M2 1l6 6-6 6" fill="none" stroke="#888" stroke-width="2.5"/></svg></div>
</section>

<div class="feature" style="left:64px">
  <div class="feature-icon"><svg width="16" height="16" viewBox="0 0 16 16"><path d="M3 13 10 6M9 2a3 3 0 0 0 4 4" stroke="#999" stroke-width="2.5" fill="none" stroke-linecap="round"/></svg></div>
  <h3>Coaching</h3>
  <p>Marketing coaching and consulting services that accelerate book sales.</p>
</div>
<div class="feature" style="left:364px">
  <div class="feature-icon"><svg width="16" height="16" viewBox="0 0 16 16"><circle cx="8" cy="8" r="4" fill="none" stroke="#999" stroke-width="2"/><path d="M8 1v3M8 12v3M1 8h3M12 8h3" stroke="#999" stroke-width="2"/></svg></div>
  <h3>Ideal Readers</h3>
  <p>Target your ideal reader and grow fans who promote your book for you.</p>
</div>
<div class="feature" style="left:664px">
  <div class="feature-icon"><svg width="16" height="16" viewBox="0 0 16 16"><path d="M3 13 11 5" stroke="#999" stroke-width="2.5" stroke-linecap="round"/><path d="M12 1v3M10.5 2.5h3" stroke="#999" stroke-width="1.5"/></svg></div>
  <h3>Low Cost</h3>
  <p>High impact, low cost strategies that achieve your goals and fit your budget.</p>
</div>

<div class="section-rule" style="left:64px;top:560px;width:836px"></div>
<h2 class="section-title" style="top:549px">Dorothy’s Popular Talks</h2>
<div class="work-nav prev"><svg width="6" height="8" viewBox="0 0 6 8"><path d="M5 0 1 4l4 4" fill="none" stroke="#aaa" stroke-width="1.5"/></svg></div>
<div class="work-nav next"><svg width="6" height="8" viewBox="0 0 6 8"><path d="M1 0l4 4-4 4" fill="none" stroke="#fff" stroke-width="1.5"/></svg></div>

<article class="work-card" style="left:64px">
  <div class="work-image" role="img" aria-label="Green maple leaves against soft light" style="background:radial-gradient(circle at 60% 40%,#e8f4b8,#8cc43a 55%,#4f8a1c)"></div>
  <h4>The Power of Pagehive</h4><span>Speaking</span>
</article>
<article class="work-card" style="left:289px">
  <div class="work-image" role="img" aria-label="Person lying on a sofa using a phone" style="background:linear-gradient(135deg,#d9d6d2,#b9b3ac 50%,#6e6a66)"></div>
  <h4>Simplify Social Media</h4><span>Speaking</span>
</article>
<article class="work-card" style="left:515px">
  <div class="work-image" role="img" aria-label="Orange wall with a round chair and pendant lamp" style="background:linear-gradient(180deg,#e98a45,#d8652a 75%,#e9e2dc 76%)"></div>
  <h4>The Ideal Author Website</h4><span>Speaking</span>
</article>
<article class="work-card" style="left:740px">
  <div class="work-image" role="img" aria-label="Glass skyscrapers seen from below against blue sky" style="background:linear-gradient(160deg,#2c5d8f,#5d95c7 50%,#bcd8ef)"></div>
  <h4>Succeed on Bazario</h4><span>Speaking</span>
</article>

<div class="section-rule" style="left:64px;top:850px;width:886px"></div>
<h2 class="section-title" style="top:838px">Our Clients</h2>
<svg class="clients-arrow" style="left:63px" width="8" height="12" viewBox="0 0 8 12"><path d="M7 1 2 6l5 5" fill="none" stroke="#bbb" stroke-width="1.5"/></svg>
<div class="client" style="left:133px"><i class="mark"></i>brightnode</div>
<div class="client" style="left:300px;font-size:15px">NIGHTPERCH</div>
<div class="client" style="left:454px"><i class="mark"></i>LOOPWAY</div>
<div class="client" style="left:618px"><i class="mark"></i>roastly</div>
<div class="client" style="left:776px"><i class="mark"></i>ELLIPSA</div>
<svg class="clients-arrow" style="left:943px" width="8" height="12" viewBox="0 0 8 12"><path d="M1 1l5 5-5 5" fill="none" stroke="#bbb" stroke-width="1.5"/></svg>

<footer class="site-footer">
  <div class="foot-col" style="left:64px">
    <h5>About</h5>
    <p>Want to be a best selling author, but need someone to show you the way? Are you ready for results? Call now for a free consultation.</p>
  </div>
  <div class="foot-col" style="left:289px">
    <h5>Testimonials</h5>
    <p class="quote"><svg width="11" height="9" viewBox="0 0 11 9"><path d="M0 9V5C0 2 1.5.5 4 0v2C2.8 2.4 2.4 3.2 2.4 4H4v5zM7 9V5c0-3 1.5-4.5 4-5v2c-1.2.4-1.6 1.2-1.6 2H11v5z" fill="#999"/></svg>Dorothy made marketing my novel simple, and my sales took off fast.<cite>— Indie author</cite></p>
  </div>
  <div class="foot-col" style="left:515px">
    <h5>Get In Touch</h5>
    <div class="contact-row"><svg width="8" height="11" viewBox="0 0 8 11"><path d="M4 11S0 6 0 4a4 4 0 0 1 8 0c0 2-4 7-4 7z" fill="#999"/></svg><b>Address:</b> Example.com</div>
    <div class="contact-row" style="margin-top:21px"><svg width="10" height="10" viewBox="0 0 10 10"><path d="M2 0l2 2.5-1.2 1.3a6 6 0 0 0 3.4 3.4L7.5 6 10 8 8.6 10C4 9.6.4 6 0 1.4z" fill="#999"/></svg><b>Phone:</b> 214-555-0183</div>
    <div class="contact-row" style="margin-top:8px"><svg width="11" height="8" viewBox="0 0 11 8"><rect width="11" height="8" fill="#999"/><path d="M0 0l5.5 4L11 0" fill="none" stroke="#f5f5f5"/></svg><b>Email:</b> mail@example.com</div>
  </div>
  <div class="foot-col" style="left:740px">
    <h5>Newsletter</h5>
    <p>Sign up for our free newsletter and receive our list of Top Chirpnet Tips for Authors Free!</p>
    <div class="newsletter-form"><div class="field">mail@example.com</div><div class="go">Go</div></div>
  </div>
</footer>

<div class="bottom-bar">
  <div class="copyright">© Copyright 2013</div>
  <div class="social"><em class="connect" style="font-style:normal">Connect with Dorothy:</em><span>Chirpnet</span><span>Friendwall</span><span>Orbix+</span><span>Workloop</span><span>RSS</span></div>
</div>

</body>
</html>
```